Marina Web Page

I'm looking for a visually engaging web page/layout that I can use as the basis for a website for my Marina. I need to include page content that can be stored and updated in an include file to allow someone to easily manage content without editing html or needing to understand html.

The business is a small marina and fishing center located on the Pamlico sound in eastern North Carolina right off the Intracoastal Waterway. We offer wet slips with power, water, and wifi and also have powered RV slips for camping available. The Marina sells fuel, beer, tackle/bait, and ice. The Marina also has an island style bar (The Gullwing Bar) and live music most weekends. The bar has a mascot named Dusty, short for captain, who is a black labradoodle know for diving to the bottom of the marina basin to retrieve oysters and rocks. Dusty could be incorporated as a minor design element but isn't a requirement.The marina caters to coastal sportsmen interested in sound fishing as well as offshore sport fishing. The Marina also offers fishing charters form a 32' Brinewood fishing boat w/ tuna tower.

The primary purpose of the initial version of the website is to communicate information about up coming events, music, bar specials etc... It will also be used to feature our services, fishing report and weather info, where we are located from both land and water, and a photo gallery.

Target Market(s)

Coastal sports enthusiast and the coastal boating community

Industry/Entity Type

Business

Requirements
Must have
• I would like animated menus incorporated into the page temple. It must also allow for the updating/storing of page content in a separate file to that an employee of the marina can update specials and events without having to understand or edit html.
Nice to have
• A photo gallery option that will present photos from a folder on the web server. Changing photos should be as easy as adding or deleting photos from the folder.

```html
<!DOCTYPE html>
<html lang="en">
<head>
<meta charset="utf-8">
<title>Harbor Point Marina</title>
<link rel="stylesheet" href="https://fonts.googleapis.com/css2?family=Arimo:wght@400;700&family=Open+Sans:wght@300;400;600&display=swap">
<style>
:root{
  --blue:#2a6ab4;
  --nav-yellow:#f5c000;
  --green:#3cbd7c;
  --teal:#31a8bb;
  --magenta:#c0336a;
  --rust:#c2542f;
  --weather:#8190d0;
  --weather-head:#7280bf;
  --text:#1b1b1b;
  --rule:#cfcfcf;
  --footer:#f4f4f4;
}
*{margin:0;padding:0;box-sizing:border-box}
html,body{width:1200px;height:1200px;overflow:hidden}
body{
  position:relative;
  font-family:"Arimo",Arial,sans-serif;
  color:var(--text);
  background:linear-gradient(180deg,#6fb9e4 0%,#8fcbe9 30%,#3f8db9 55%,#1f5f7f 72%,#0c2d3b 85%,#06161d 100%);
}
.abs{position:absolute}
.page{left:120px;top:0;width:960px;height:1162px;background:#fff}
.footer-band{left:120px;top:891px;width:960px;height:271px;background:var(--footer)}
.hero{left:134px;top:0;width:932px;height:422px;
  background:linear-gradient(160deg,#6d8697 0%,#4d6675 40%,#8fa3ae 70%,#dfe6ea 100%)}
.logo-box{left:146px;top:0;width:178px;height:112px;background:#fff;display:flex;align-items:center;justify-content:center;gap:6px}
.logo-box .dot{width:12px;height:12px;border-radius:50%;background:var(--blue)}
.logo-box span{font-weight:700;font-size:17px;color:var(--blue);line-height:1.1;text-align:center}
.nav{left:333px;top:37px;width:733px;height:47px;background:var(--blue);border-bottom:9px solid var(--nav-yellow);
  display:flex;justify-content:space-around;align-items:center;padding:0 8px 0 4px}
.nav a{color:#fff;text-decoration:none;font-size:13px}
.tile{top:436px;width:220px;height:159px}
.tile .photo{height:126px}
.tile .label{height:33px;color:#fff;font-size:13px;display:flex;align-items:center;justify-content:center}
.rule{height:1px;background:var(--rule)}
h2{position:absolute;font-weight:400;font-size:16px;letter-spacing:.2px}
.event{left:134px;width:458px}
.date{position:absolute;left:0;top:0;width:75px;height:75px;background:var(--blue);color:#fff;text-align:center;font-family:"Open Sans",sans-serif}
.date .day{font-size:36px;line-height:44px;display:block;margin-top:2px}
.date .mon{font-size:19px;line-height:20px;display:block;letter-spacing:-.5px}
.event h3{position:absolute;left:87px;top:2px;font-size:13px;font-weight:700;color:var(--blue)}
.event p{position:absolute;left:87px;top:20px;width:372px;font-size:12.4px;line-height:18.7px}
.weather{left:608px;top:664px;width:458px;height:189px;background:var(--weather);color:#fff;font-family:"Open Sans",sans-serif}
.weather .city{height:23px;background:var(--weather-head);text-align:center;font-size:13px;font-weight:600;line-height:23px}
.now{position:absolute;left:19px;top:30px;font-size:62px;font-weight:300;line-height:1}
.now sup,.fc sup{font-size:.32em;vertical-align:top;position:relative;top:.1em;margin-left:4px}
.cond{position:absolute;right:19px;top:36px;text-align:right;font-size:14px;line-height:18px}
.weather .line{position:absolute;left:19px;right:19px;top:120px;height:1px;background:rgba(255,255,255,.3)}
.fc{position:absolute;top:132px;text-align:center;font-size:26px;font-weight:300;line-height:1}
.fc small{display:block;font-size:9.5px;font-weight:400;margin-top:1px}
.field{left:149px;width:305px;height:28px;border:1px solid #cfcfcf;background:#fff;font-size:12.5px;color:#555;padding:6px 9px}
.send{left:149px;top:1101px;width:54px;height:28px;background:var(--nav-yellow);color:#fff;font-size:13px;border:1px solid #e2b100;display:flex;align-items:center;justify-content:center}
.contact-row{left:607px;display:flex;align-items:center;gap:10px;font-size:12.5px}
.contact-row svg{width:20px;height:20px}
.social{left:607px;top:1081px;display:flex;gap:12px}
.social i{width:14px;height:14px;border-radius:50%;background:var(--nav-yellow);display:block}
.copy{right:135px;top:1082px;font-size:12.5px}
</style>
</head>
<body>
<div class="abs page"></div>
<div class="abs footer-band"></div>

<div class="abs hero" role="img" aria-label="Sport fishing boat with tuna tower running across open water"></div>
<div class="abs logo-box"><div class="dot"></div><span>Harbor Point<br>Marina</span></div>
<nav class="abs nav">
  <a href="#">ABOUT</a><a href="#">SERVICES</a><a href="#">EVENTS</a><a href="#">FISHING REPORT</a><a href="#">WEATHER INFO</a><a href="#">GALLERY</a><a href="#">CONTACT US</a>
</nav>

<div class="abs tile" style="left:134px">
  <div class="photo" role="img" aria-label="Scuba diver underwater with a lionfish" style="background:linear-gradient(135deg,#0d6fb8,#1d9be0)"></div>
  <div class="label" style="background:var(--green)">DIVING FOR FISH</div>
</div>
<div class="abs tile" style="left:371px">
  <div class="photo" role="img" aria-label="Tents pitched on a green field by the trees" style="background:linear-gradient(180deg,#c8e6f2 0%,#3a7a3a 45%,#6cc43a 100%)"></div>
  <div class="label" style="background:var(--teal)">CAMPING</div>
</div>
<div class="abs tile" style="left:608px">
  <div class="photo" role="img" aria-label="Band playing outdoors at sunset" style="background:linear-gradient(180deg,#d8633a 0%,#5a3a3a 45%,#2a241e 100%)"></div>
  <div class="label" style="background:var(--magenta)">LIVE MUSIC</div>
</div>
<div class="abs tile" style="left:846px">
  <div class="photo" role="img" aria-label="Wooden bar counter with shelves of bottles" style="background:linear-gradient(180deg,#3a2418 0%,#7a4a2a 60%,#4a5a6a 100%)"></div>
  <div class="label" style="background:var(--rust)">BAR SPECIAL</div>
</div>

<div class="abs rule" style="left:134px;top:614px;width:932px"></div>

<h2 style="left:134px;top:630px">UPCOMING EVENTS</h2>
<div class="abs event" style="top:664px">
  <div class="date"><span class="day">20</span><span class="mon">AUG 03</span></div>
  <h3>NAME OF EVENTS</h3>
  <p>Lorem ipsum dolor sit amet, consectetur adipisicing elit, sed do eiusmod tempor incididunt ut labore et dolore magna aliqua. Ut enim ad minim veniam</p>
</div>
<div class="abs rule" style="left:134px;top:758px;width:458px"></div>
<div class="abs event" style="top:776px">
  <div class="date"><span class="day">25</span><span class="mon">SEP 03</span></div>
  <h3>NAME OF EVENTS</h3>
  <p>Lorem ipsum dolor sit amet, consectetur adipisicing elit, sed do eiusmod tempor incididunt ut labore et dolore magna aliqua. Ut enim ad minim veniam</p>
</div>

<h2 style="left:608px;top:630px">WEATHER FORECAST</h2>
<div class="abs weather">
  <div class="city">MTL</div>
  <div class="now">45<sup>F</sup></div>
  <div class="cond">overcast clouds<br>humidity: 70%<br>wind: 0mph ENE<br>H 46 • L 44</div>
  <div class="line"></div>
  <div class="fc" style="left:56px">48<sup>F</sup><small>WED</small></div>
  <div class="fc" style="left:208px">35<sup>F</sup><small>THU</small></div>
  <div class="fc" style="left:361px">31<sup>F</sup><small>FRI</small></div>
</div>

<h2 style="left:148px;top:917px">SEND INQUIRY</h2>
<div class="abs field" style="top:951px">Name</div>
<div class="abs field" style="top:988px">E-mail</div>
<div class="abs field" style="top:1026px;width:427px;height:66px">Message</div>
<div class="abs send">SEND</div>

<h2 style="left:607px;top:917px">CONTACT US</h2>
<div class="abs contact-row" style="top:951px">
  <svg viewBox="0 0 20 20"><path d="M10 2 1 10h3v8h4.5v-5h3v5H16v-8h3z" fill="var(--blue)"/></svg>
  <span>Name of Street Number #12, Name of City, Name of Country, ZIP Code</span>
</div>
<div class="abs contact-row" style="top:984px">
  <svg viewBox="0 0 20 20"><rect x="1" y="4" width="18" height="12" fill="var(--blue)"/><path d="M1 4l9 7 9-7" fill="none" stroke="#fff" stroke-width="1.4"/></svg>
  <span>info@harborpoint-example.com</span>
</div>
<div class="abs contact-row" style="top:1017px">
  <svg viewBox="0 0 20 20"><path d="M2 7c0-2 3-3 8-3s8 1 8 3v2h-4V7H6v2H2z" fill="var(--blue)"/><rect x="4" y="10" width="12" height="7" rx="1" fill="var(--blue)"/><circle cx="10" cy="13.5" r="2" fill="#fff"/></svg>
  <span>(555) 014 3456 7890 / (555) 098 7654 321</span>
</div>
<div class="abs rule" style="left:607px;top:1062px;width:459px"></div>
<div class="abs social"><i></i><i></i><i></i></div>
<div class="abs copy">Copyright (c) harborpoint-example.com 2013. All rights reserved.</div>
</body>
</html>
```